Verdant Loop Advisors, LLC

I am looking for a simple, clear layout with my logo prominent and embossed, on the best quality card stock available. I would like the business name and phone number included on the card as well......I dont want my name anywhere on the card and I would like my logo embossed on the card......something simple with a white back......open to designs as long as they go along with recycling symbols and green type stuff.....The address, website, cell number, fax number, and email are listed below

5374 Tillbury Fenwood Road
Fernhollow, MD 20999

c. 240.555.0143 f. 240.555.0187
e. sales@verdantloopadvisors.example
w. www.verdantloopadvisors.example

Industry/Entity Type

Recycling

```html
<!DOCTYPE html>
<html lang="en">
<head>
<meta charset="utf-8">
<title>Verdant Loop Advisors, LLC — Business Card</title>
<link rel="stylesheet" href="https://fonts.googleapis.com/css2?family=Archivo:wght@500;700;800&display=swap">
<style>
  :root {
    --backdrop: #2b2d2b;
    --card-white: #ffffff;
    --charcoal: #33393c;
    --ink: #24282a;
    --leaf: #3d8a2f;
    --lime-tint: #cfe095;
    --on-dark: #ffffff;
  }
  * { margin: 0; padding: 0; box-sizing: border-box; }
  html, body {
    width: 1200px; height: 959px; overflow: hidden;
    background: var(--backdrop);
    font-family: "Archivo", Arial, sans-serif;
  }
  .card {
    position: absolute; left: 100px; top: 194px;
    width: 1000px; height: 571px;
    background: var(--card-white);
    overflow: hidden;
    box-shadow: 0 10px 30px rgba(0,0,0,.45);
  }
  .card-shapes { position: absolute; inset: 0; }
  .brand {
    position: absolute; left: 60px; top: 52px;
    display: flex; align-items: center; gap: 22px;
  }
  .brand-dot {
    width: 62px; height: 62px; border-radius: 50%;
    background: var(--leaf); flex: none;
  }
  .brand-name {
    font-weight: 800; font-size: 40px; letter-spacing: .5px;
    text-transform: uppercase; color: var(--ink); white-space: nowrap;
  }
  .address {
    position: absolute; left: 60px; top: 245px;
    font-style: normal;
    color: var(--on-dark); font-weight: 500; font-size: 30px; line-height: 1.25;
  }
  .contact-line {
    position: absolute; display: flex; align-items: center;
    color: var(--on-dark); font-weight: 500; white-space: nowrap;
  }
  .contact-line svg { flex: none; }
  .phone-cell { left: 615px; top: 316px; font-size: 31px; gap: 18px; }
  .phone-fax  { left: 610px; top: 370px; font-size: 31px; gap: 18px; }
  .email      { left: 110px; top: 378px; font-size: 22px; gap: 16px; }
  .website {
    position: absolute; left: 100px; top: 493px;
    font-weight: 700; font-size: 34px; color: var(--ink); white-space: nowrap;
  }
</style>
</head>
<body>
  <article class="card">
    <svg class="card-shapes" width="1000" height="571" viewBox="0 0 1000 571" aria-hidden="true">
      <path class="accent-band" fill="var(--lime-tint)"
            d="M0,160 C350,205 700,200 1000,148 L1000,240 C700,214 350,204 0,200 Z"/>
      <path class="dark-panel" fill="var(--charcoal)"
            d="M0,200 C350,206 700,216 1000,236 L1000,468 C700,452 350,432 0,418 Z"/>
      <path class="accent-rule" fill="none" stroke="var(--lime-tint)" stroke-width="6"
            d="M0,430 C350,444 700,464 1000,482"/>
      <rect class="bottom-edge" x="0" y="554" width="1000" height="17" fill="var(--lime-tint)"/>
    </svg>

    <div class="brand">
      <span class="brand-dot"></span>
      <span class="brand-name">Verdant Loop Advisors, LLC</span>
    </div>

    <address class="address">
      5374 Tillbury Fenwood Road<br>Fernhollow, MD 20999
    </address>

    <div class="contact-line phone-cell">
      <svg width="24" height="36" viewBox="0 0 24 36" aria-label="Cell">
        <rect x="2" y="2" width="20" height="32" rx="4" fill="none" stroke="var(--lime-tint)" stroke-width="3"/>
        <line x1="9" y1="29" x2="15" y2="29" stroke="var(--lime-tint)" stroke-width="2.5"/>
      </svg>
      <span>240.555.0143</span>
    </div>

    <div class="contact-line phone-fax">
      <svg width="34" height="30" viewBox="0 0 34 30" aria-label="Fax">
        <rect x="8" y="1" width="18" height="10" fill="none" stroke="var(--lime-tint)" stroke-width="2.5"/>
        <rect x="1" y="11" width="32" height="12" rx="2" fill="var(--lime-tint)"/>
        <rect x="7" y="19" width="20" height="10" fill="var(--lime-tint)" stroke="var(--charcoal)" stroke-width="2"/>
      </svg>
      <span>240.555.0187</span>
    </div>

    <div class="contact-line email">
      <svg width="34" height="24" viewBox="0 0 34 24" aria-label="Email">
        <rect x="1" y="1" width="32" height="22" fill="var(--lime-tint)"/>
        <path d="M1,1 L17,14 L33,1" fill="none" stroke="var(--charcoal)" stroke-width="2"/>
      </svg>
      <span>sales@verdantloopadvisors.example</span>
    </div>

    <p class="website">www.verdantloopadvisors.example</p>
  </article>
</body>
</html>
```